Handy man Company business card

need branded business card for my new company, this design will transfer to car wrap design what winner will be asked to design

I will need original file so I can edit it in the end.

Also like to have some inspirational quote like "ONE CALL WE DO IT ALL"
"We do it right" can be added to logo side

Like to try to see large 1 800 000 0000 number on front with large logo

Size bigger then standard business card

I like to integrate LAS VEGAS sign to one of sides

Target Market(s)

Handy man services, Home renovation and remodeling

Industry/Entity Type

Handyman

Contact Information for Business Card

Tool Baron LLC.
Name: BORIS LENKOVA
Phone "Temporary": 000 000 0000
Adress: 2715 Fenmore Ct, Las Vegas NV 89147
Website: www.toolbaron.vegas
Email: info@toolbaron.vegas

Requirements
Must have
• Two side
• side n1: LOGO
• side n2: INFO
Nice to have
• Like to have some interesting idea for client to remember!
• With logo added to both side at different stile
Should not have
• Standard design,

```html
<!DOCTYPE html>
<html lang="en">
<head>
<meta charset="utf-8">
<title>Tool Baron LLC. — Business Card</title>
<link rel="stylesheet" href="https://fonts.googleapis.com/css2?family=Open+Sans:wght@400;600;700&display=swap">
<style>
  :root {
    --backdrop: #e7e4e0;
    --card: #0d0d0d;
    --card-edge: #1a1a1a;
    --gold: #f2a823;
    --gold-line: #b97d13;
    --text-light: #f1ece6;
    --text-soft: #d9d6d2;
    --figure-cap: #f3a928;
    --figure-skin: #f6d7b0;
    --figure-shirt: #8fcdea;
  }
  * { box-sizing: border-box; margin: 0; padding: 0; }
  html, body { width: 1200px; height: 900px; overflow: hidden; }
  body {
    background: var(--backdrop);
    font-family: "Open Sans", Arial, sans-serif;
    display: flex;
    align-items: center;
    justify-content: center;
    gap: 48px;
  }
  .card {
    position: relative;
    width: 540px;
    height: 310px;
    background: var(--card);
    border: 1px solid var(--card-edge);
    box-shadow: 0 10px 28px rgba(0,0,0,.25);
    overflow: hidden;
  }

  /* Info side */
  .mascot-area {
    position: absolute;
    left: 40px;
    bottom: 0;
    width: 210px;
    height: 270px;
    border-radius: 100px 100px 0 0;
    background: linear-gradient(180deg, var(--figure-cap) 0%, var(--figure-skin) 35%, var(--figure-shirt) 58%, var(--figure-cap) 80%);
    opacity: .9;
  }
  .info-divider {
    position: absolute;
    left: 282px;
    top: 70px;
    width: 1px;
    height: 150px;
    background: linear-gradient(180deg, transparent, var(--gold-line) 20%, var(--gold-line) 80%, transparent);
  }
  .info-block {
    position: absolute;
    left: 304px;
    top: 70px;
    color: var(--text-soft);
    font-size: 13px;
    line-height: 1.35;
  }
  .holder-name {
    color: var(--gold);
    font-weight: 600;
    font-size: 15px;
    letter-spacing: .3px;
    margin-bottom: 24px;
  }
  .address { margin-bottom: 14px; }
  .contact-list { list-style: none; }
  .contact-list li { display: flex; align-items: center; gap: 8px; }
  .contact-list svg { width: 10px; height: 10px; flex: none; }

  /* Logo side */
  .brand-lockup {
    position: absolute;
    left: 150px;
    top: 82px;
    display: flex;
    align-items: center;
    gap: 16px;
  }
  .brand-mascot {
    width: 46px;
    height: 74px;
    border-radius: 22px 22px 6px 6px;
    background: linear-gradient(180deg, var(--figure-cap) 0%, var(--figure-skin) 35%, var(--figure-shirt) 55%, var(--figure-cap) 80%);
  }
  .brand-name {
    color: var(--text-light);
    font-weight: 700;
    font-size: 38px;
    letter-spacing: .5px;
  }
  .tagline {
    position: absolute;
    left: 0;
    right: 0;
    top: 210px;
    text-align: center;
    color: #ffffff;
    font-weight: 600;
    font-size: 15px;
    letter-spacing: .4px;
  }
</style>
</head>
<body>

  <section class="card card--info" aria-label="Contact side">
    <div class="mascot-area" role="img" aria-label="Cartoon handyman mascot in a yellow cap and overalls holding a hammer and giving a thumbs up"></div>
    <div class="info-divider"></div>
    <div class="info-block">
      <p class="holder-name">BORIS LENKOVA</p>
      <p class="address">2715 Fenmore Ct, Las Vegas<br>NV 89147</p>
      <ul class="contact-list">
        <li>
          <svg viewBox="0 0 10 10" aria-hidden="true"><path d="M2 0.8 L3.6 0.8 L4.2 3 L3 3.8 Q4 6 6.2 7 L7 5.8 L9.2 6.4 L9.2 8 Q9.2 9.2 8 9.2 Q1 8.6 0.8 2 Q0.8 0.8 2 0.8Z" fill="var(--gold)"/></svg>
          1 800 000 0000
        </li>
        <li>
          <svg viewBox="0 0 10 10" aria-hidden="true"><rect x="0.5" y="2" width="9" height="6.5" fill="var(--gold)"/><path d="M0.8 2.3 L5 5.6 L9.2 2.3" fill="none" stroke="var(--card)" stroke-width="0.9"/></svg>
          info@toolbaron.vegas
        </li>
        <li>
          <svg viewBox="0 0 10 10" aria-hidden="true"><circle cx="5" cy="5" r="4.5" fill="var(--gold)"/><path d="M0.5 5 H9.5 M5 0.5 Q2.2 5 5 9.5 M5 0.5 Q7.8 5 5 9.5" fill="none" stroke="var(--card)" stroke-width="0.7"/></svg>
          www.toolbaron.vegas
        </li>
      </ul>
    </div>
  </section>

  <section class="card card--brand" aria-label="Logo side">
    <div class="brand-lockup">
      <div class="brand-mascot" role="img" aria-label="Small cartoon handyman mascot"></div>
      <span class="brand-name">Tool Baron</span>
    </div>
    <p class="tagline">ONE CALL WE DO IT ALL</p>
  </section>

</body>
</html>
```